CBD Boutique Business Card Needed

We are in need of a business card to reflect the direction of our latest products. We are a fully organic company in which our store and products are very heavy in wood and "natural" components. We decided to bring color into one of our brands and immediately knew this is where we needed to go.

We are NOT a cash grab CBD company. We could have done this wrong, slapped a label on a shit product and left it like that. I am passionate about sharing my experience with other veterans and opening a store and making it a comfortable place for others to come and see if they can have the same experience.

Target Market(s)

We are a dual market company. We do have a beauty line that will cover the costs of the majority of our business. But we also heavily cater to veterans and first responders. I am a veteran and this is how I found out about CBD. So the marketing needs to bring in our higher end beauty clientele but also be able to not put off our customers that readily need this.

Contact Information for Business Card

What we are looking for is a light, professional, boutique design that is is neither quite feminine or masculine. Attached is a picture of a store in Portland that we asked our store designer to get her inspiration from. But all natural wood and black outlines are what is mostly in there.

Attached are the following files:

Logo: An AI file with how we have our logo. I do not understand AI and have no idea why the letters are individual. The font is Adam. OLU is the logo and Tonics of Vigor is our tagline.

KM Vantage (front and back) cards I did originally found at a trade show that I absolutely loved...while it is mostly there and I would still be happy with them but it is me pretending to be you. I understand I am not and there is probably a lot wrong that all of you would see instantly and this is why I am here.

Dropper Bottle: This is our final product mock up

Water Color: I am semi flexible here. This water color is slightly different on every level of our brand. The color itself can change...we are not stuck on THIS particular one. If you happen to make a new one that is similar in style and we use it...then I will happily commission you to change the rest on our next product run. I am pretty sure you can use this statement as evidence later . =) .

But seriously, we heavily believe in pay it forward and will work with anyone here that may have a vision bigger than ours. The winner of this contest will get preferential consideration on our marketing materials (need letterhead etc. next, as well as a brochure, and website) so three more projects coming down the pipeline.

Information to use for your mockup is contained on the card images I have included. I would prefer CBD for wellness CBD for life to be more prominent. No where else on the card do we have CBD mentioned.

Font styles to use
Sans Serif

Colors

Designer to choose colors to be used in the design.

Requirements
Must have
• Double Sided
• Front: OLU logo on front of card will be raised embossed. Background is watercolor. One has been provided. Others are up for consideration. If the rest of your design is incredible and I don't like your watercolor I will just ask to swap it.
• Back: Standard information. Not stuck on anything here. I LOVE clean minimal designs. The bleed on the card I provided is a luxury...
• Font for title and OLU is Adam. Everything else I prefer san serif or as clean as possible.
Nice to have
• I Need to incorporate Naturally Nurturing somewhere on the card. Bold but not intrusive.

```html
<!DOCTYPE html>
<html lang="en">
<head>
<meta charset="utf-8">
<title>OLU – Tonics of Vigor Business Card</title>
<link rel="stylesheet" href="https://fonts.googleapis.com/css2?family=Montserrat:wght@300;400&display=swap">
<style>
  :root {
    --page-bg: #d9d9d9;
    --card-bg: #ffffff;
    --ink: #1b1b1b;
    --ink-soft: #3a3a3a;
    --wash-yellow: #f4e76a;
    --wash-green: #b9dc8f;
    --wash-teal: #a9dde0;
    --wash-pink: #eeb6c8;
    --wash-lilac: #b9b5e6;
  }
  * { box-sizing: border-box; margin: 0; padding: 0; }
  html, body { width: 1200px; height: 932px; overflow: hidden; }
  body {
    background: var(--page-bg);
    font-family: "Montserrat", sans-serif;
    color: var(--ink);
    position: relative;
  }
  .card {
    position: absolute;
    top: 86px;
    width: 436px;
    height: 760px;
    border-radius: 26px;
    background: var(--card-bg);
    overflow: hidden;
    box-shadow: 0 14px 34px rgba(0,0,0,0.22);
  }
  .card--front { left: 118px; }
  .card--back { left: 646px; }

  .watercolor-full {
    position: absolute; inset: 0;
    background:
      radial-gradient(ellipse 45% 30% at 30% 12%, var(--wash-yellow) 0%, transparent 70%),
      radial-gradient(ellipse 40% 25% at 80% 20%, var(--wash-yellow) 0%, transparent 70%),
      radial-gradient(ellipse 30% 20% at 62% 38%, var(--wash-pink) 0%, transparent 75%),
      radial-gradient(ellipse 35% 22% at 55% 48%, var(--wash-lilac) 0%, transparent 75%),
      radial-gradient(ellipse 60% 35% at 35% 45%, var(--wash-green) 0%, transparent 75%),
      radial-gradient(ellipse 60% 35% at 45% 72%, var(--wash-teal) 0%, transparent 75%),
      var(--card-bg);
  }
  .front-logo {
    position: absolute;
    left: 0; right: 0; top: 330px;
    text-align: center;
  }
  .brand-name {
    font-weight: 300;
    font-size: 104px;
    letter-spacing: 14px;
    line-height: 1;
    padding-left: 14px;
  }
  .brand-tagline {
    margin-top: 14px;
    font-weight: 300;
    font-size: 28px;
    letter-spacing: 3px;
    text-transform: uppercase;
  }

  .wash-corner {
    position: absolute; top: 0; right: 0;
    width: 260px; height: 360px;
    background:
      radial-gradient(ellipse 50% 40% at 70% 30%, var(--wash-teal) 0%, transparent 70%),
      radial-gradient(ellipse 40% 30% at 60% 55%, var(--wash-pink) 0%, transparent 70%),
      radial-gradient(ellipse 55% 40% at 75% 75%, var(--wash-yellow) 0%, transparent 70%),
      radial-gradient(ellipse 45% 40% at 40% 40%, var(--wash-green) 0%, transparent 70%);
  }
  .wash-bottom {
    position: absolute; left: 0; right: 0; bottom: 0;
    height: 190px;
    background:
      radial-gradient(ellipse 35% 55% at 85% 45%, var(--wash-yellow) 0%, transparent 70%),
      radial-gradient(ellipse 35% 55% at 50% 80%, var(--wash-green) 0%, transparent 70%),
      radial-gradient(ellipse 30% 50% at 20% 90%, var(--wash-yellow) 0%, transparent 70%),
      radial-gradient(ellipse 30% 45% at 65% 95%, var(--wash-teal) 0%, transparent 70%);
  }
  .back-logo {
    position: absolute; left: 48px; top: 70px;
  }
  .back-logo .brand-name { font-size: 70px; letter-spacing: 9px; padding-left: 0; text-align: left; }
  .back-logo .brand-tagline { font-size: 19px; margin-top: 8px; letter-spacing: 2px; }

  .person {
    position: absolute; left: 86px; top: 330px;
  }
  .person-name {
    font-weight: 400; font-size: 26px; letter-spacing: 1px;
    text-transform: uppercase; color: var(--ink-soft);
  }
  .person-title {
    margin-top: 6px; font-weight: 400; font-size: 16px;
    letter-spacing: 1.5px; text-transform: uppercase; color: var(--ink-soft);
  }
  .contact-list {
    position: absolute; left: 74px; top: 440px;
    list-style: none;
  }
  .contact-item {
    display: flex; align-items: center;
    margin-bottom: 42px;
    font-size: 15px; line-height: 1.45; color: var(--ink-soft);
  }
  .contact-icon { width: 24px; height: 24px; flex: none; }
  .contact-divider {
    width: 1px; height: 40px; background: var(--ink-soft);
    margin: 0 16px 0 14px; flex: none;
  }
</style>
</head>
<body>

  <section class="card card--front" aria-label="Card front">
    <div class="watercolor-full" role="img" aria-label="Soft watercolor wash in yellow, green, teal and pink"></div>
    <div class="front-logo">
      <div class="brand-name">OLU</div>
      <div class="brand-tagline">Tonics of Vigor</div>
    </div>
  </section>

  <section class="card card--back" aria-label="Card back">
    <div class="wash-corner" role="img" aria-label="Watercolor wash in teal, pink, green and yellow"></div>
    <div class="wash-bottom" role="img" aria-label="Watercolor wash in yellow, green and teal"></div>

    <div class="back-logo">
      <div class="brand-name">OLU</div>
      <div class="brand-tagline">Tonics of Vigor</div>
    </div>

    <div class="person">
      <div class="person-name">Dana Whitfield</div>
      <div class="person-title">Owner / CEO</div>
    </div>

    <ul class="contact-list">
      <li class="contact-item">
        <svg class="contact-icon" viewBox="0 0 24 24" aria-hidden="true">
          <path d="M12 2a7 7 0 0 0-7 7c0 5 7 13 7 13s7-8 7-13a7 7 0 0 0-7-7z" fill="#2a2a2a"/>
          <circle cx="12" cy="9" r="3" fill="#fff"/>
        </svg>
        <span class="contact-divider"></span>
        <span>4120 W Juniper Ave<br>Peoria, AZ 85345, Suite 210</span>
      </li>
      <li class="contact-item">
        <svg class="contact-icon" viewBox="0 0 24 24" aria-hidden="true">
          <path d="M6.6 10.8a15 15 0 0 0 6.6 6.6l2.2-2.2a1 1 0 0 1 1-.25 11 11 0 0 0 3.6.6 1 1 0 0 1 1 1V20a1 1 0 0 1-1 1A17 17 0 0 1 3 4a1 1 0 0 1 1-1h3.5a1 1 0 0 1 1 1 11 11 0 0 0 .6 3.6 1 1 0 0 1-.25 1z" fill="#2a2a2a"/>
        </svg>
        <span class="contact-divider"></span>
        <span>602.555.0148</span>
      </li>
      <li class="contact-item">
        <svg class="contact-icon" viewBox="0 0 24 24" aria-hidden="true">
          <circle cx="12" cy="12" r="10" fill="#2a2a2a"/>
          <g fill="none" stroke="#fff" stroke-width="1.2">
            <ellipse cx="12" cy="12" rx="4.5" ry="10"/>
            <line x1="2" y1="12" x2="22" y2="12"/>
            <path d="M4 7h16M4 17h16"/>
          </g>
        </svg>
        <span class="contact-divider"></span>
        <span>hello@olu.life<br>www.olu.life</span>
      </li>
    </ul>
  </section>

</body>
</html>
```